Website for "Centro de Tecnicas Verdales"

We need a new web design for an enterprise dedicated to environment and energy saving engineering, based in Monterrey, Mexico.
They offer consulting services, mainly to enhance building designs, and they are also resellers for several products in the energy saving field.

The final design should be oriented to engineers and architects, and should communicate professionalism, innovation, environment care.

Here is the website of a partner enterprise, which does pretty much the same:

http://www.brisatermica.example/

Target Market(s)

mainly architects and engineers looking for solutions on energy efficiency building

Industry/Entity Type

Environment

Requirements
Must have
• Entry page must be quite graphical and intuitive, must have a "products listing" and a "projects portfolio".

```html
<!DOCTYPE html>
<html lang="it">
<head>
<meta charset="utf-8">
<title>Centro de Tecnicas Verdales</title>
<link rel="stylesheet" href="https://fonts.googleapis.com/css2?family=Arimo:wght@400;700&family=Oswald:wght@400;500&family=Montserrat:wght@700&display=swap">
<style>
:root{
  --blue:#00a7d6;
  --blue-band:rgba(0,170,214,.85);
  --orange:#f07023;
  --green:#8cc63f;
  --green-dark:#6cb33f;
  --purple:#4b3f8f;
  --ink:#333;
  --grey:#777;
  --card:#efecec;
  --white:#fff;
}
*{margin:0;padding:0;box-sizing:border-box}
html,body{width:1200px;height:1200px;overflow:hidden;background:var(--white);font-family:Arimo,Arial,sans-serif;color:var(--ink)}
.page{position:relative;width:1200px;height:1200px}

.brand{position:absolute;left:216px;top:38px;display:flex;align-items:center;gap:10px}
.brand-dot{width:44px;height:44px;border-radius:50%;background:var(--blue)}
.brand-name{font-family:Oswald,sans-serif;font-size:17px;font-weight:500;color:var(--ink);line-height:1.1;width:170px}

.nav{position:absolute;right:217px;top:55px;display:flex;gap:18px;font-family:Oswald,sans-serif;font-size:13px;letter-spacing:.3px}
.nav a{color:#555;text-decoration:none;padding-bottom:7px}
.nav a.current{color:var(--blue);border-bottom:3px solid var(--blue);padding:0 12px 7px}
.login{position:absolute;right:217px;top:84px;font-family:Montserrat,sans-serif;font-size:13px;color:var(--green);letter-spacing:1px}

.hero{position:absolute;left:0;top:126px;width:1200px;height:468px;background:linear-gradient(160deg,#e6edf3 0%,#7ea4c8 30%,#2f6aa8 60%,#3a3f45 100%)}
.hero-band{position:absolute;left:486px;top:32px;right:0;height:96px;background:var(--blue-band);padding:22px 0 0 23px;font-family:Montserrat,sans-serif;font-size:17px;letter-spacing:1.6px;color:var(--white);line-height:31px}
.hero-btn{position:absolute;left:792px;top:283px;width:138px;height:50px;background:var(--orange);color:var(--white);font-size:15px;font-weight:400;display:flex;align-items:center;justify-content:center}

.intro{position:absolute;left:216px;top:610px;width:574px}
.intro h1{font-size:22px;font-weight:700;color:#444;margin-bottom:12px}
.intro p{font-size:10px;font-weight:700;line-height:24px;color:#444}

.services{position:absolute;left:216px;top:742px;display:flex;gap:11px}
.service{width:184px;height:180px;background:var(--card);padding:22px 18px 0 22px}
.service h2{font-family:Oswald,sans-serif;font-size:12px;font-weight:400;margin-bottom:16px}
.service p{font-size:9.6px;line-height:14.4px;color:#111}
.t-blue{color:var(--blue)}.t-orange{color:var(--orange)}.t-purple{color:var(--purple)}

.slider{position:absolute;left:216px;top:934px;width:574px;height:143px;background:var(--card)}
.slider-photo{position:absolute;left:0;top:0;width:137px;height:143px;background:linear-gradient(180deg,#e8eef6,#6d8fb8 55%,#7a8a4c)}
.arrow{position:absolute;top:64px}
.slide-col{position:absolute;top:12px;font-size:9.6px;line-height:14.4px;color:var(--grey)}

.news{position:absolute;left:798px;top:620px;width:185px;height:457px;background:var(--blue);color:var(--white)}
.news h2{height:38px;background:var(--orange);font-family:Oswald,sans-serif;font-size:21px;font-weight:500;text-align:center;line-height:38px;letter-spacing:1px}
.news-item{padding:8px 13px 0 13px;font-size:10.6px;line-height:14.4px}
.news-item h3{font-size:10.6px;font-weight:700;letter-spacing:.4px;color:#e9f7fb}
.news-item .date{color:#111}
.more{display:block;text-align:right;color:#e7ff3a;font-size:9.5px;margin-top:2px}

.ground{position:absolute;left:0;bottom:0}
.tree{position:absolute;left:216px;top:1094px;width:128px;height:106px;background:var(--green-dark);border-radius:50% 50% 6px 6px}
.windmill{position:absolute;left:920px;top:1088px;width:56px;height:108px;background:var(--green);border-radius:28px 28px 0 0}
.social{position:absolute;left:808px;top:1110px;display:flex;gap:4px}
.social span{width:33px;height:33px;border-radius:50%;background:var(--green-dark)}
.copy{position:absolute;left:0;width:1226px;top:1181px;text-align:center;font-size:8px;color:#333;letter-spacing:.3px}
</style>
</head>
<body>
<div class="page">
  <header>
    <div class="brand"><span class="brand-dot"></span><span class="brand-name">Centro de Tecnicas Verdales</span></div>
    <nav class="nav">
      <a class="current">HOME</a><a>PRODUCTO</a><a>PROJECTS PORTFOLIO</a><a>CONTACTO</a><a>SERVICIO</a>
    </nav>
    <div class="login">LOGIN</div>
  </header>

  <section class="hero" role="img" aria-label="Photo of a windmill rotor seen from below against a cloudy blue sky">
    <div class="hero-band">LOREM IPSUM DOLOR SIT AMET,<br>CONSECTETUER ADIPISCING ELIT. NAM</div>
    <div class="hero-btn">CLICK HERE</div>
  </section>

  <section class="intro">
    <h1>Centro Tecnico per l'Energia di Verdalia</h1>
    <p>E' una società di ingegneria a responsabilità limitata, costituita nel 2001, operante in tutti i campi dell'ingegneria energetica a servizio di aziende, consorzi, industrie, privati e pubbliche amministrazioni. La società è in grado di svolgere qualsiasi attività tecnica nel settore dell'energia. Visualizza la brochure completa.</p>
  </section>

  <section class="services">
    <article class="service"><h2 class="t-blue">EFFICIENZA ENERGETICA</h2><p>La società effettua analisi di efficienza energetica termica ed elettrica in ambito civile e industriale, proponendo interventi di miglioramento tecnico e gestionale per la riduzione di consumi e costi.</p></article>
    <article class="service"><h2 class="t-orange">MERCATO DELL'ENERGIA</h2><p>La società effettua analisi di efficienza energetica termica ed elettrica in ambito civile e industriale, proponendo interventi di miglioramento tecnico e gestionale per la riduzione di consumi e costi.</p></article>
    <article class="service"><h2 class="t-purple">PROGETTAZIONE IMPIANTI</h2><p>La società effettua analisi di efficienza energetica termica ed elettrica in ambito civile e industriale, proponendo interventi di miglioramento tecnico e gestionale per la riduzione di consumi e costi.</p></article>
  </section>

  <section class="slider">
    <div class="slider-photo" role="img" aria-label="Photo of a solar panel array in a field"></div>
    <svg class="arrow" style="left:147px" width="12" height="16" viewBox="0 0 12 16"><path d="M9 2 3 8l6 6" fill="none" stroke="#111" stroke-width="2.5"/></svg>
    <div class="slide-col" style="left:170px;width:110px">Progettazione<br>Le competenze<br>tecniche degli<br>ingegneri del<br>Centro Tecnico<br>per l'Energia<br>consentono la<br>progettazione...</div>
    <div class="slide-col" style="left:304px;width:120px">Efficienza e<br>risparmio<br>energetico<br>La società effettua<br>analisi di<br>efficienza<br>energetica termica<br>ed elettrica in</div>
    <div class="slide-col" style="left:451px;width:100px;top:15px">Mercato<br>dell'Energia<br>elettrica e del<br>Gas:<br>aggiornamenti<br>tariffari...<br>Per gli utenti del<br>dispacciamento si</div>
    <svg class="arrow" style="left:555px" width="12" height="16" viewBox="0 0 12 16"><path d="M3 2l6 6-6 6" fill="none" stroke="#111" stroke-width="2.5"/></svg>
  </section>

  <aside class="news">
    <h2>NEWS</h2>
    <div class="news-item">
      <h3>Sospensione dell'erogazione degli incentivi per mancato adeguamento alle prescrizioni dell'Allegato A.70 del Codice di Rete ai sensi della delibera 84/2012/R/eel</h3>
      <div class="date">2013-06-10</div>
      <div>by Centro Verdales</div>
      <div>Con riferimento al comunicato pubblicato sul sito internet del GRT il 13 marzo 2013,"Adeguamento impianti in media tensione con potenza superiore a 50...</div>
      <a class="more">more</a>
    </div>
    <div class="news-item" style="padding-top:0">
      <h3>Interventi relativi agli impianti di generazione distribuita per garantire la sicurezza del sistema elettrico nazionale</h3>
      <div class="date">2013-06-13</div>
      <div>by Centro Verdales</div>
      <div>I produttori di energia da fonti rinnovabili saranno</div>
      <a class="more" style="margin-top:14px">more</a>
    </div>
  </aside>

  <footer>
    <svg class="ground" width="1200" height="44" viewBox="0 0 1200 44"><path d="M0 20 C300 20 400 0 700 0 C900 0 1000 12 1200 16 L1200 44 L0 44Z" fill="var(--green)"/></svg>
    <div class="tree" role="img" aria-label="Illustration of a tree beside a small house"></div>
    <div class="windmill" role="img" aria-label="Illustration of a farm windmill tower"></div>
    <div class="social"><span></span><span></span><span></span></div>
    <div class="copy">COPYRIGHTS 2013, ALL RIGHTS RESERVED</div>
  </footer>
</div>
</body>
</html>
```